Dental specialist needs a sharp looking letterhead

I am looking for a letterhead to be used to send letters and communication between myself (a dental specialist) and other dentists.
My office is a state of the art dental specialty office.
I need to letterhead to also state:
Gideon R. Whitfield DDS
2847 Birchmont Avenue, Suite K
West Harlow, NY 14391
(716)482-9163
fax: (716)482-9170
whitfieldroot.com (**this email address may change)

i included my logo designs.
thank you

Target Market(s)

dentists

Industry/Entity Type

Communication

Requirements
Must have
• the included logo, whether the vertical or horizontal versions

```html
<!DOCTYPE html>
<html lang="en">
<head>
<meta charset="utf-8">
<title>Lakeridge Endodontics P.C. – Letterhead</title>
<link rel="stylesheet" href="https://fonts.googleapis.com/css2?family=Source+Sans+3:wght@400;600;700&display=swap">
<style>
  :root {
    --sky: #d5eafb;
    --paper: #ffffff;
    --ink: #1b1b1b;
    --navy: #1f2a44;
    --brand-blue: #3fb6ec;
    --lime: #b6f040;
  }
  html, body {
    margin: 0;
    padding: 0;
    width: 852px;
    height: 1200px;
    overflow: hidden;
    background: var(--paper);
  }
  .letterhead {
    position: relative;
    width: 852px;
    height: 1200px;
    overflow: hidden;
    background: var(--paper);
    font-family: "Source Sans 3", "Myriad Pro", Arial, sans-serif;
    color: var(--ink);
  }
  .bands {
    position: absolute;
    inset: 0;
    width: 852px;
    height: 1200px;
  }
  .brand {
    position: absolute;
    left: 40px;
    top: 70px;
    display: flex;
    align-items: center;
    gap: 14px;
  }
  .brand-dot {
    width: 52px;
    height: 52px;
    border-radius: 50%;
    background: var(--brand-blue);
    flex: none;
  }
  .brand-name {
    font-weight: 600;
    font-size: 27px;
    line-height: 30px;
    color: var(--navy);
    letter-spacing: 0.5px;
  }
  .contact {
    position: absolute;
    right: 45px;
    top: 8px;
    text-align: right;
    font-size: 18px;
    line-height: 26px;
    color: var(--ink);
  }
  .contact .doctor {
    font-weight: 700;
  }
  .body-copy {
    position: absolute;
    left: 36px;
    top: 250px;
    font-size: 22px;
    line-height: 35.5px;
    color: var(--ink);
  }
  .body-copy p {
    margin: 0 0 26px;
    white-space: nowrap;
  }
  .tooth-motif {
    position: absolute;
    left: 561px;
    top: 1051px;
    width: 192px;
    height: 106px;
    border-radius: 18px;
    background: radial-gradient(ellipse at center, rgba(182, 240, 64, 0.55), rgba(182, 240, 64, 0.15));
  }
</style>
</head>
<body>
<div class="letterhead">
  <svg class="bands" viewBox="0 0 852 1200" aria-hidden="true">
    <path d="M0 0 H852 V218 C720 200 560 190 420 196 C260 203 120 220 0 236 Z" fill="var(--sky)"/>
    <path d="M0 1088 C150 1070 330 1062 500 1064 C640 1066 760 1058 852 1030 V1200 H0 Z" fill="var(--sky)"/>
  </svg>

  <div class="brand">
    <span class="brand-dot"></span>
    <span class="brand-name">Lakeridge<br>Endodontics P.C.</span>
  </div>

  <address class="contact" style="font-style: normal;">
    <div class="doctor">Gideon R. Whitfield DDS</div>
    <div>2847 Birchmont Avenue, Suite K</div>
    <div>West Harlow, NY 14391</div>
    <div>Phone: (716)482-9163</div>
    <div>Fax: (716)482-9170</div>
    <div>whitfieldroot.com</div>
  </address>

  <main class="body-copy">
    <p>Lorem ipsum dolor sit amet, vix in purto tollit deseruisse, iusto omnium<br>
    cetero sit ad, vel ea vivendum platonem adipiscing. His et graecis eloquen-<br>
    tiam, eu quem indoctum sea. Ad dolor appetere deseruisse usu. Eu vix<br>
    munere omnium nonumes, aeque eruditi liberavisse est ad. His ei fabulas<br>
    delicatissimi. Te vis eius dolore, aperiam salutandi vim at, et his mazim gloria-<br>
    tur. Quo ut possim appetere inciderint.</p>
    <p>Ne iusto expetenda consetetur vim, an unum eirmod eum. Malis scriptorem<br>
    est no, posse graeco nominati ad quo, est etiam delectus aliquando cu. Nos-<br>
    trud laoreet perfecto ex eos, an mel oratio soleat. Et laudem percipit elo-<br>
    quentiam mea, quodsi definitionem sit eu. No populo pertinacia interesset<br>
    quo. Alia conclusionemque sea cu.</p>
    <p>Vel cibo admodum facilisis ex, has te natum utinam. Quo suas electram no,<br>
    euismod indoctum ne nam. Sed ex ullum utinam, lorem aeterno albucius his<br>
    ne. His ad voluptua patrioque torquatos. Mea vidit harum gubergren at, ne<br>
    ipsum epicurei mandamus sed, ea unum percipit senserit mea. Ex per mazim<br>
    tamquam veritus.</p>
    <p>Pri ancillae delicatissimi cu. Vide facete tibique et ius. Cu his reque reformi-<br>
    dans, at vel doctus concludaturque. An abhorreant assueverit honestatis has.</p>
  </main>

  <div class="tooth-motif" role="img" aria-label="Lime green line illustration of a tooth with small dotted circles on either side"></div>
</div>
</body>
</html>
```